Business Cards for a start up company

We are looking for a business card design for a start up company based in Ohio. The logo is attached. We are a healthcare company. We are open to all designs but want something professional but fun; creative, not boring

Industry/Entity Type

Healthcare

```html
<!DOCTYPE html>
<html lang="en">
<head>
<meta charset="utf-8">
<title>Brightpath Health Plus – Business Cards</title>
<link href="https://fonts.googleapis.com/css2?family=Tinos:wght@700&family=Questrial&display=swap" rel="stylesheet">
<style>
  :root {
    --backdrop: #b3a57c;
    --card: #f7f7f8;
    --card-shade: #ececef;
    --navy: #35336f;
    --green: #8cc43f;
    --ink: #1f1f24;
    --muted: #3c3c46;
  }
  html, body {
    margin: 0;
    width: 1200px;
    height: 800px;
    overflow: hidden;
    background: var(--backdrop);
  }
  .canvas {
    position: relative;
    width: 1200px;
    height: 800px;
  }
  .card {
    position: absolute;
    width: 560px;
    height: 320px;
    background: linear-gradient(135deg, #ffffff 0%, var(--card) 55%, var(--card-shade) 100%);
    box-shadow: 0 14px 28px rgba(40, 30, 10, 0.35);
    overflow: hidden;
  }
  .card--front { left: 70px; top: 60px; }
  .card--back { left: 570px; top: 420px; }

  .brand-name {
    font-family: "Tinos", "Times New Roman", serif;
    font-weight: 700;
    color: var(--navy);
    margin: 0;
    white-space: nowrap;
  }
  .brand-dot {
    display: inline-block;
    border-radius: 50%;
    background: var(--green);
    vertical-align: middle;
  }

  /* Front */
  .front-band {
    position: absolute;
    left: 0; top: 0;
    width: 180px; height: 320px;
    background: var(--navy);
  }
  .front-brand {
    position: absolute;
    right: 40px;
    top: 120px;
    text-align: right;
  }
  .front-brand .brand-dot { width: 46px; height: 46px; margin-bottom: 10px; }
  .front-brand .brand-name { font-size: 30px; }
  .front-web {
    font-family: "Questrial", "Century Gothic", sans-serif;
    font-size: 16px;
    color: var(--navy);
    margin-top: 14px;
    letter-spacing: 0.3px;
  }

  /* Back */
  .back-brand {
    position: absolute;
    left: 60px; top: 50px;
    display: flex;
    align-items: center;
    gap: 16px;
  }
  .back-brand .brand-dot { width: 52px; height: 52px; }
  .back-brand .brand-name { font-size: 30px; }

  .contact {
    position: absolute;
    top: 175px;
    font-family: "Questrial", "Century Gothic", sans-serif;
    font-size: 14px;
    color: var(--ink);
    line-height: 26px;
  }
  .contact--lines {
    right: 280px;
    text-align: right;
  }
  .contact-row {
    display: flex;
    align-items: center;
    justify-content: flex-end;
    gap: 12px;
  }
  .contact-icon { width: 14px; height: 14px; fill: var(--ink); flex: none; }
  .contact--address {
    left: 300px;
    display: flex;
    gap: 10px;
  }
  .contact--address .contact-icon { margin-top: 6px; }
  .contact--address p { margin: 0; }
</style>
</head>
<body>
<main class="canvas">

  <section class="card card--front" aria-label="Business card front">
    <div class="front-band"></div>
    <div class="front-brand">
      <span class="brand-dot"></span>
      <h1 class="brand-name">Brightpath Health Plus</h1>
      <div class="front-web">www.brightpathhealth.com</div>
    </div>
  </section>

  <section class="card card--back" aria-label="Business card back">
    <div class="back-brand">
      <span class="brand-dot"></span>
      <h2 class="brand-name">Brightpath Health Plus</h2>
    </div>

    <div class="contact contact--lines">
      <div class="contact-row">
        <span>+1 614.555.0172</span>
        <svg class="contact-icon" viewBox="0 0 24 24" aria-hidden="true"><path d="M6.6 10.8a15.1 15.1 0 0 0 6.6 6.6l2.2-2.2a1 1 0 0 1 1-.25 11.4 11.4 0 0 0 3.6.57 1 1 0 0 1 1 1V20a1 1 0 0 1-1 1A17 17 0 0 1 3 4a1 1 0 0 1 1-1h3.5a1 1 0 0 1 1 1c0 1.25.2 2.45.57 3.57a1 1 0 0 1-.25 1z"/></svg>
      </div>
      <div class="contact-row">
        <span>hello@brightpathhealth.com</span>
        <svg class="contact-icon" viewBox="0 0 24 24" aria-hidden="true"><path d="M2 5h20v14H2z" fill="none" stroke="currentColor"/><path d="M2 5h20v14H2V5zm2 2v.5l8 5 8-5V7H4z"/></svg>
      </div>
      <div class="contact-row">
        <span>www.brightpathhealth.com</span>
        <svg class="contact-icon" viewBox="0 0 24 24" aria-hidden="true"><path d="M12 2a10 10 0 1 0 0 20 10 10 0 0 0 0-20zm6.9 6h-3a15.7 15.7 0 0 0-1.4-3.6A8 8 0 0 1 18.9 8zM12 4c.8 1.2 1.5 2.5 1.9 4h-3.8c.4-1.5 1.1-2.8 1.9-4zM4.3 14a8 8 0 0 1 0-4h3.4a16 16 0 0 0 0 4zm.8 2h3a15.7 15.7 0 0 0 1.4 3.6A8 8 0 0 1 5.1 16zm3-8h-3a8 8 0 0 1 4.4-3.6A15.7 15.7 0 0 0 8.1 8zM12 20c-.8-1.2-1.5-2.5-1.9-4h3.8c-.4 1.5-1.1 2.8-1.9 4zm2.3-6H9.7a14.7 14.7 0 0 1 0-4h4.6a14.7 14.7 0 0 1 0 4zm.2 5.6a15.7 15.7 0 0 0 1.4-3.6h3a8 8 0 0 1-4.4 3.6zm1.8-5.6a16 16 0 0 0 0-4h3.4a8 8 0 0 1 0 4z"/></svg>
      </div>
    </div>

    <div class="contact contact--address">
      <svg class="contact-icon" viewBox="0 0 24 24" aria-hidden="true"><path d="M12 2a7 7 0 0 0-7 7c0 5.2 7 13 7 13s7-7.8 7-13a7 7 0 0 0-7-7zm0 9.5A2.5 2.5 0 1 1 12 6.5a2.5 2.5 0 0 1 0 5z"/></svg>
      <div>
        <p>210 Maple Grove Ave, Suite 4</p>
        <p>Columbus, Ohio 43215</p>
      </div>
    </div>
  </section>

</main>
</body>
</html>
```